Webdesign/ Redesign of community frontpage (only design, no code!)

Our social community website (http://www.tavoro.eu) needs a fresh, more invitating frontpage. Our audience are 14 - 25 year old.

Only the screen design (psd & image) is needed, no code (no html, no css, ...).

Style:
- Modern/ clear/ lightweight/ invitating design for young people
- Emphasize the intent of the website (social community website, meeting other young people to chat, hangout, ..)
- Optimized for 1024x768

Elements that must appear:
- Logo (attached as EPS, can be modified if needed)
- Login form (Username, Password, Status/Feeling, Forgot password link, ...)
- Link to registration page OR registration form
- Empty space (around 350x250 pixel) where a video or other dynamic content could be embedded (done by myself)
- Five feature/pro statements (max. 60 letters each, not necessarily to be displayed as a group, see below)
- Currently present links in footer
- Some statistics (Number of people online, total number of members (females/ males))

Elements that might appear:
- Registration form instead of link to separate registration form (ex like chatterbox has it)

Ideas:
- Registration form could also be designed to be a layer that'll show when the user clicks
- If the design needs/allows it, I can also animate random member photos (80x80 pixels) and place them on the frontpage using js/ ajax

Feature/pro statements examples (see above):
- Dauerhaft kostenlos für Frauen und Männer
- Reale Profile, extrem wenig Fakes & Störenfriede
- Persönliches Profil mit vielen Funktionen
- Hoher Schutz deiner Privatsphäre und Daten
- Viele freundliche Mitarbeiter und Helfer
Updates

After having reviewed the first two designs, I'd like to give these general ideas/ feedback:

1. I think it would be much better to _not_ have the whole registration form on the frontpage but instead only a link which opens the form in a layer/dialog when clicked. Of course only the design of the dialog needs to be done, I'll do the actual coding. To have a first impression of how the dialog could look like, please see the newly attached dialog.png (the text in the dialog is just for demo and should be replaced by the actual registration form).

2. There should be no separation between males/ females like it is currently. I think it'd better to mix because it emphasizes the community/ group character of the site and does not make it look too much like da dating site.

3. I think the five statements/ pros I mentioned (why should people register, what are the greatest features of our site, ..) could be best displayed as balloon tips (just like in comics) next to some images of users.

4. The color of the site should not be too heavy and should make people feel comfortable.

5. The logo provied must be fixed to read "TAVORO.eu" instead of "LUNEPA.de". I hope this i no big deal, sorry for that. This could also be done afterwards for a small additional amount of money, as it doesn't really affect the overall design.

To better illustrate all my writings above I just made two simple sketches and attached them (frontpage.png and frontpage_with_active_registration.png).

Important: these only show all the elements that must appear on the page and what I thought might be a good idea of how to present the pros/ features of my site. The actual placements, sizes, arragements etc. can of course all be different.

Looking forward to your create additions and design skills to make this look pretty... :-)

Just to emphasize, the design should not look or feel heavy. So please keep the colors light/ soft, no huge images, don't stretch the logo to much, etc.

Please do not insert any content (like search boxes, text blocks, etc.) which is not already present in my mockups. The only thing that should be additionally added is a link/ button so people can login using keypass (chatterbox, searchly, ..) too.

Target Market(s)

Young people 14 - 25 years old interested in meeting friends, new people, chat, flirt, hangout, have fun.

Industry/Entity Type

Community

Requirements
Must have
• see description
Nice to have
• see description
Should not have
• plugin dependencies (ex flash)

```html
<!DOCTYPE html>
<html lang="en">
<head>
<meta charset="utf-8">
<title>TAVORO.de – chat, flirt &amp; more</title>
<link rel="stylesheet" href="https://fonts.googleapis.com/css2?family=Arimo:wght@400;700&family=Marcellus&display=swap">
<style>
  :root {
    --sky-top: #cdeefb;
    --sky-bottom: #ffffff;
    --ink: #1d1d1d;
    --text: #333333;
    --muted: #555555;
    --brand-blue: #1fa9e1;
    --bubble-top: #5ccdf3;
    --bubble-bottom: #17a3da;
    --bubble-edge: #1192c6;
    --alert-red: #e8120c;
    --button-red: #e41b12;
    --video-blue: #86d3f3;
    --map-tone: #dbe9ef;
    --stats-top: #58cdf3;
    --stats-bottom: #17a2d9;
  }
  * { box-sizing: border-box; margin: 0; padding: 0; }
  html, body { width: 1200px; height: 800px; overflow: hidden; }
  body {
    position: relative;
    font-family: "Arimo", Arial, sans-serif;
    color: var(--text);
    background: linear-gradient(to bottom, var(--sky-top) 0, #e6f7fd 260px, var(--sky-bottom) 520px);
  }

  /* Brand */
  .brand { position: absolute; left: 122px; top: 30px; width: 370px; height: 100px; }
  .brand__mark {
    position: absolute; left: 0; top: 8px; width: 34px; height: 34px;
    background: var(--ink);
  }
  .brand__name {
    position: absolute; left: 48px; top: 0;
    font-family: "Arimo", Arial, sans-serif; font-weight: 400;
    font-size: 46px; color: var(--ink); line-height: 1;
  }
  .brand__tagline {
    position: absolute; left: 0; top: 68px;
    font-family: "Arimo", Arial, sans-serif; font-weight: 400;
    font-size: 22px; color: var(--muted); line-height: 1;
  }

  /* Login */
  .login {
    position: absolute; left: 658px; top: 22px; width: 412px; height: 94px;
    background: linear-gradient(to bottom, #ffffff, #f1f1f1);
    border: 1px solid #e2e2e2; border-radius: 8px;
    box-shadow: 0 12px 14px -10px rgba(120, 190, 220, .55);
  }
  .login__field {
    position: absolute; height: 24px; width: 133px;
    border: 1px solid #bdbdbd; background: #fff;
    font-size: 11px; color: #222; padding: 5px 9px; line-height: 13px;
  }
  .login__field--user { left: 16px; top: 15px; }
  .login__field--pass { left: 159px; top: 15px; }
  .login__field--status { left: 16px; top: 51px; }
  .login__field--status svg { position: absolute; right: 7px; top: 8px; }
  .login__forgot {
    position: absolute; left: 305px; top: 20px; font-size: 11px;
    color: var(--alert-red); text-decoration: underline;
  }
  .login__remember { position: absolute; left: 160px; top: 57px; font-size: 11px; color: #222; }
  .login__remember span {
    display: inline-block; width: 10px; height: 10px; border: 1px solid #aaa;
    background: #fff; vertical-align: -1px; margin-right: 4px;
  }
  .login__button {
    position: absolute; left: 263px; top: 51px; width: 66px; height: 25px;
    background: linear-gradient(to bottom, #ff3a2e, var(--button-red) 55%, #c8100a);
    border-radius: 3px; color: #fff; font-size: 11px; font-weight: 700;
    text-align: center; line-height: 25px;
  }

  /* Main panel */
  .panel {
    position: absolute; left: 110px; top: 157px; width: 980px; height: 623px;
    background: linear-gradient(to bottom, #ffffff 0, #fbfbfb 240px, #ececec 550px);
    border-radius: 8px; box-shadow: 0 0 6px rgba(0, 0, 0, .18);
    overflow: hidden;
  }
  .intro__title {
    position: absolute; left: 20px; top: 32px;
    font-family: "Marcellus", serif; font-weight: 400;
    font-size: 40px; color: var(--brand-blue); line-height: 1;
  }
  .intro__lead {
    position: absolute; left: 20px; top: 82px;
    font-family: "Marcellus", serif; font-size: 24px; color: var(--ink); line-height: 1;
  }
  .signup__title {
    position: absolute; left: 625px; top: 38px;
    font-family: "Arimo", Arial, sans-serif; font-weight: 400;
    font-size: 39px; color: var(--alert-red); line-height: 1;
  }
  .signup__link {
    position: absolute; left: 625px; top: 85px; font-size: 18px; color: var(--muted);
    text-decoration: underline;
  }

  .worldmap {
    position: absolute; left: 15px; top: 148px; width: 570px; height: 240px;
    background: radial-gradient(ellipse at center, var(--map-tone), rgba(219, 233, 239, 0) 70%);
    opacity: .7;
  }

  .member {
    position: absolute; width: 91px; height: 91px; background: #fff;
    padding: 5px; box-shadow: 0 1px 4px rgba(0, 0, 0, .25);
  }
  .member__photo { width: 100%; height: 100%; }
  .member--a { left: 40px; top: 146px; }
  .member--a .member__photo { background: linear-gradient(#7bb04a, #b49a84); }
  .member--b { left: 480px; top: 146px; }
  .member--b .member__photo { background: linear-gradient(#4a3a30, #9c7e6a); }
  .member--c { left: 230px; top: 276px; }
  .member--c .member__photo { background: linear-gradient(#eadfd3, #d7b79d); }
  .member--d { left: 40px; top: 369px; }
  .member--d .member__photo { background: linear-gradient(#f2efec, #a0775c); }
  .member--e { left: 470px; top: 366px; }
  .member--e .member__photo { background: linear-gradient(#5d5d5d, #c9b6a8); }

  .bubble {
    position: absolute; padding: 0 10px; font-size: 14px; line-height: 18px; color: #fff;
    background: linear-gradient(to bottom, var(--bubble-top), var(--bubble-bottom));
    border: 1px solid var(--bubble-edge); border-radius: 5px;
    display: flex; align-items: center;
  }
  .bubble::after {
    content: ""; position: absolute; width: 0; height: 0;
    border: 7px solid transparent;
  }
  .bubble--a { left: 124px; top: 149px; width: 185px; height: 38px; }
  .bubble--a::after { left: -13px; top: 12px; border-right-color: var(--bubble-top); }
  .bubble--b { left: 307px; top: 235px; width: 262px; height: 38px; }
  .bubble--b::after { left: 218px; top: -13px; border-bottom-color: var(--bubble-top); }
  .bubble--c { left: 27px; top: 253px; width: 254px; height: 38px; }
  .bubble--c::after { left: 210px; bottom: -14px; border-top-color: var(--bubble-bottom); }
  .bubble--d { left: 209px; top: 382px; width: 267px; height: 56px; }
  .bubble--d::after { right: -14px; top: 8px; border-left-color: var(--bubble-top); }
  .bubble--e { left: 37px; top: 459px; width: 262px; height: 56px; }
  .bubble--e::after { left: 20px; top: -13px; border-bottom-color: var(--bubble-top); }

  .video {
    position: absolute; left: 592px; top: 145px; width: 367px; height: 293px;
    background: #fff; padding: 8px; box-shadow: 0 0 5px rgba(0, 0, 0, .2);
  }
  .video__screen { position: relative; width: 350px; height: 251px; background: var(--video-blue); }
  .video__screen svg { position: absolute; left: 113px; top: 66px; }
  .video__controls {
    height: 27px; display: flex; align-items: center;
    background: linear-gradient(to bottom, #f4f4f4, #cfcfcf); border: 1px solid #b5b5b5;
  }
  .video__btn { width: 30px; height: 25px; display: flex; align-items: center; justify-content: center; border-right: 1px solid #b5b5b5; }
  .video__time { font-size: 11px; color: #222; padding: 0 8px 0 4px; }
  .video__track { flex: 1; height: 6px; background: #9a9a9a; border-radius: 3px; position: relative; margin-right: 12px; }
  .video__knob { position: absolute; left: -4px; top: -4px; width: 14px; height: 14px; border-radius: 50%; background: #777; border: 2px solid #ddd; }
  .video__up { width: 24px; height: 16px; margin-right: 3px; background: linear-gradient(#fafafa, #cfcfcf); border: 1px solid #999; border-radius: 3px; display: flex; align-items: center; justify-content: center; }

  .video-note {
    position: absolute; left: 601px; top: 451px; width: 360px;
    font-size: 12px; line-height: 18px; color: #444;
  }

  .stats {
    position: absolute; left: 0; bottom: 0; width: 980px; height: 70px;
    background: linear-gradient(to bottom, var(--stats-top), var(--stats-bottom));
  }
  .stat {
    position: absolute; top: 13px; display: flex; align-items: center; gap: 8px;
    color: #fff; font-size: 18px; font-weight: 700; text-shadow: 0 1px 1px rgba(0, 70, 110, .5);
  }
  .stat--all { left: 25px; }
  .stat--male { left: 237px; }
  .stat--female { left: 487px; }
  .stat--online { left: 757px; }

  .footer {
    position: absolute; top: 793px; left: 119px; width: 962px;
    font-size: 9px; color: #222; display: flex; justify-content: space-between;
  }
</style>
</head>
<body>

<header class="brand">
  <span class="brand__mark"></span>
  <div class="brand__name">TAVORO.de</div>
  <div class="brand__tagline">chat, flirt &amp; more</div>
</header>

<form class="login">
  <div class="login__field login__field--user">Username</div>
  <div class="login__field login__field--pass">Password</div>
  <a class="login__forgot">Forgot Password?</a>
  <div class="login__field login__field--status">Status/Feeling
    <svg width="9" height="6" viewBox="0 0 9 6"><path d="M0 0h9L4.5 6z" fill="#222"/></svg>
  </div>
  <label class="login__remember"><span></span>Remember Me</label>
  <div class="login__button">LOGIN</div>
</form>

<main class="panel">
  <h1 class="intro__title">TAVORO helps you to</h1>
  <p class="intro__lead">connect and share with the people in your life.</p>

  <h2 class="signup__title">No Account Yet?</h2>
  <a class="signup__link">Sign up - It’s free and always will be!</a>

  <div class="worldmap" role="img" aria-label="Faint world map in the background"></div>

  <div class="member member--a"><div class="member__photo" role="img" aria-label="Member photo of a smiling young man"></div></div>
  <div class="member member--b"><div class="member__photo" role="img" aria-label="Member photo of a young man with dark hair"></div></div>
  <div class="member member--c"><div class="member__photo" role="img" aria-label="Member photo of a blonde young woman"></div></div>
  <div class="member member--d"><div class="member__photo" role="img" aria-label="Member photo of a smiling young woman"></div></div>
  <div class="member member--e"><div class="member__photo" role="img" aria-label="Member photo of a young man in shirt and tie"></div></div>

  <p class="bubble bubble--a">I like how they care of you</p>
  <p class="bubble bubble--b">It’s just the best communityi know off ;)</p>
  <p class="bubble bubble--c">I like it beacause its free for everyone</p>
  <p class="bubble bubble--d">So many great features, like webcam chat, image galleries, games, ...</p>
  <p class="bubble bubble--e">So many great features, like webcam chat, image galleries, games, ...</p>

  <section class="video">
    <div class="video__screen" role="img" aria-label="Video area with play button">
      <svg width="124" height="124" viewBox="0 0 124 124">
        <defs>
          <linearGradient id="playGloss" x1="0" y1="0" x2="0" y2="1">
            <stop offset="0" stop-color="#ffffff" stop-opacity=".85"/>
            <stop offset="1" stop-color="#c6ccd2" stop-opacity=".75"/>
          </linearGradient>
        </defs>
        <circle cx="62" cy="62" r="59" fill="url(#playGloss)" stroke="#d9dde1" stroke-width="4"/>
        <path d="M48 36 L92 62 L48 88 Z" fill="#ffffff"/>
      </svg>
    </div>
    <div class="video__controls">
      <div class="video__btn"><svg width="11" height="12" viewBox="0 0 11 12"><path d="M0 0L11 6L0 12z" fill="#333"/></svg></div>
      <div class="video__btn"><svg width="18" height="12" viewBox="0 0 18 12"><path d="M0 4h4l5-4v12l-5-4H0z" fill="#333"/><path d="M11 4v4M13 3v6M15 2v8M17 1v10" stroke="#333" stroke-width="1"/></svg></div>
      <span class="video__time">0:00 / 0:31</span>
      <div class="video__track"><span class="video__knob"></span></div>
      <div class="video__up"><svg width="12" height="7" viewBox="0 0 12 7"><path d="M0 7L6 0L12 7z" fill="#222"/></svg></div>
    </div>
  </section>

  <p class="video-note">Nulla molestie pharetra porta. Quisque that is ac enim velit, sed interdum dui. Curabitur sed turpis leo. Maurisans porta, elit eget varius dapibus, ante quam tempus sapiut felis.</p>

  <section class="stats">
    <div class="stat stat--all">
      <svg width="42" height="42" viewBox="0 0 42 42">
        <circle cx="10" cy="8" r="5" fill="#f39a1e"/><circle cx="32" cy="8" r="5" fill="#f39a1e"/>
        <path d="M2 26c0-8 4-12 8-12s8 4 8 12z M24 26c0-8 4-12 8-12s8 4 8 12z" fill="#2a74c4"/>
        <circle cx="21" cy="13" r="6" fill="#f5a623"/>
        <path d="M11 42V30c0-7 5-11 10-11s10 4 10 11v12z" fill="#1d5fae"/>
      </svg>
      98,534 Member
    </div>
    <div class="stat stat--male">
      <svg width="38" height="42" viewBox="0 0 38 42">
        <circle cx="19" cy="11" r="9" fill="#f3b27a"/>
        <path d="M10 8c2-7 16-7 18 0z" fill="#5a3a1e"/>
        <path d="M2 42c0-12 8-19 17-19s17 7 17 19z" fill="#3c6fb8"/>
        <path d="M16 23h6l-3 14z" fill="#e23b2c"/>
      </svg>
      53,345 Male Member
    </div>
    <div class="stat stat--female">
      <svg width="38" height="42" viewBox="0 0 38 42">
        <path d="M7 20c0-14 5-19 12-19s12 5 12 19z" fill="#6b3d17"/>
        <circle cx="19" cy="13" r="8" fill="#f3b27a"/>
        <path d="M3 42c0-11 7-18 16-18s16 7 16 18z" fill="#8a4b1a"/>
      </svg>
      45,109 Female Member
    </div>
    <div class="stat stat--online">
      <svg width="40" height="40" viewBox="0 0 40 40">
        <circle cx="20" cy="20" r="18" fill="#ffe21c" stroke="#d9a800" stroke-width="2"/>
      </svg>
      1453 Online Now
    </div>
  </section>
</main>

<footer class="footer">
  <span>Copyright © 2010 TAVORO.de. All rights reserved</span>
  <span>Nutzungsbedingungen | Jugendschutz | Datenschutz | Kontakt</span>
</footer>

</body>
</html>
```